VEK.PRO- Daniel Whitcombe Fitness- needs a clever business card using the logo, name, info, contact

I need a business card designed for my Online Personal Training company called VEK.PRO, abbreviation for Daniel Whitcombe Fitness. My company focuses on coaching in personal health and personal growth to unleash your greatest potential. I would like to see designs that use my color scheme of a redish-orange (C:0,M:84,Y:100,K:0), grey, white, black, and my company font is OSWALD. The final design should communicate some aspects of design, health, motivation, growth, in some way. The logo is very important to the company and can be displayed in any of the colors previously mentioned. Must include the company name, my website: www.vek.example , my email: dan@vek.example

Target Market(s)

Personal health, fitness, general public, those who lack knowledge, awareness, and confidence in personal health

Industry/Entity Type

Personal Trainer

Font styles to use
Other font styles liked:
• OSWALD. (Bold, Regular, Light)

Colors
f37122
ffffff
9d9d9d
000000

Requirements
Must have
• Must include the logo, company name, my website: www.vek.example , my email: dan@vek.example
Nice to have
• Variations of the colors scheme of a redish-orange (C:0,M:84,Y:100,K:0), grey, white, black. Logo, card, or text can be in any of these colors.
• Possible quote like "Take control of your personal health to unleash your greatest potential" or "Unleashing your greatness first begins with fitness of the body and mind"

```html
<!DOCTYPE html>
<html lang="en">
<head>
<meta charset="UTF-8">
<title>VEK.PRO Business Card</title>
<link href="https://fonts.googleapis.com/css2?family=Oswald:wght@300;400;700&display=swap" rel="stylesheet">
<style>
  :root {
    --page: #e9e7e4;
    --card: #2a2a2a;
    --card-panel: #333333;
    --card-panel-edge: #232323;
    --orange: #f04e23;
    --white: #ffffff;
    --grey: #9d9d9d;
  }
  * { margin: 0; padding: 0; box-sizing: border-box; }
  html, body {
    width: 1200px;
    height: 960px;
    overflow: hidden;
    background: var(--page);
    font-family: "Oswald", sans-serif;
  }
  .canvas {
    position: relative;
    width: 1200px;
    height: 960px;
  }
  .card {
    position: absolute;
    left: 250px;
    width: 700px;
    height: 400px;
    background: var(--card);
    overflow: hidden;
    box-shadow: 0 10px 30px rgba(0,0,0,0.25);
  }
  .card-front { top: 40px; }
  .card-back { top: 520px; }
  .card-lines {
    position: absolute;
    inset: 0;
  }

  /* Front */
  .front-brand {
    position: absolute;
    left: 0;
    right: 0;
    top: 240px;
    text-align: center;
  }
  .front-name {
    color: var(--white);
    font-weight: 700;
    font-size: 64px;
    letter-spacing: 1px;
    line-height: 1;
  }
  .front-tagline {
    position: absolute;
    left: 250px;
    width: 200px;
    top: 326px;
    text-align: center;
    color: var(--white);
    font-weight: 300;
    font-size: 14px;
    text-transform: uppercase;
    letter-spacing: 0.5px;
    line-height: 1;
  }

  /* Back */
  .back-brand {
    position: absolute;
    left: 56px;
    top: 120px;
  }
  .back-name {
    color: var(--white);
    font-weight: 700;
    font-size: 68px;
    line-height: 1;
    letter-spacing: 1px;
  }
  .back-tagline {
    color: var(--white);
    font-weight: 300;
    font-size: 16px;
    text-transform: uppercase;
    letter-spacing: 0.4px;
    margin-top: 6px;
  }
  .contact-list {
    position: absolute;
    right: 48px;
    top: 250px;
    list-style: none;
  }
  .contact-item {
    display: flex;
    align-items: center;
    gap: 16px;
    color: var(--white);
    font-weight: 300;
    font-size: 20px;
    margin-bottom: 18px;
  }
  .contact-icon { width: 24px; height: 24px; }
</style>
</head>
<body>
<main class="canvas">

  <section class="card card-front" aria-label="Card front">
    <svg class="card-lines" viewBox="0 0 700 400" aria-hidden="true">
      <path d="M0 40 H240 A115 115 0 0 1 460 40 H700" fill="none" stroke="var(--orange)" stroke-width="3"/>
      <circle cx="350" cy="150" r="78" fill="var(--orange)"/>
      <path d="M0 318 H236 V346 H464 V318 H700" fill="none" stroke="var(--white)" stroke-width="2"/>
    </svg>
    <div class="front-brand">
      <div class="front-name">VEK.PRO</div>
    </div>
    <div class="front-tagline">Daniel Whitcombe Fitness</div>
  </section>

  <section class="card card-back" aria-label="Card back">
    <svg class="card-lines" viewBox="0 0 700 400" aria-hidden="true">
      <polygon points="700,180 340,180 250,400 700,400" fill="var(--card-panel)"/>
      <polyline points="340,180 250,400" fill="none" stroke="var(--card-panel-edge)" stroke-width="4"/>
      <path d="M0 36 H300 Q318 36 326 52 Q336 72 350 72 Q364 72 374 52 Q382 36 400 36 H700" fill="none" stroke="var(--orange)" stroke-width="3"/>
      <circle cx="350" cy="50" r="12" fill="none" stroke="var(--orange)" stroke-width="3"/>
    </svg>
    <div class="back-brand">
      <div class="back-name">VEK.PRO</div>
      <div class="back-tagline">Daniel Whitcombe Fitness</div>
    </div>
    <ul class="contact-list">
      <li class="contact-item">
        <svg class="contact-icon" viewBox="0 0 24 24" aria-hidden="true" fill="none" stroke="var(--white)" stroke-width="1.4">
          <circle cx="12" cy="12" r="9"/>
          <ellipse cx="12" cy="12" rx="4" ry="9"/>
          <line x1="3" y1="12" x2="21" y2="12"/>
          <line x1="5" y1="7" x2="19" y2="7"/>
          <line x1="5" y1="17" x2="19" y2="17"/>
        </svg>
        <span>www.vek.example</span>
      </li>
      <li class="contact-item">
        <svg class="contact-icon" viewBox="0 0 24 24" aria-hidden="true" fill="none" stroke="var(--white)" stroke-width="1.4">
          <rect x="2.5" y="5.5" width="19" height="13"/>
          <polyline points="2.5,5.5 12,13 21.5,5.5"/>
        </svg>
        <span>dan@vek.example</span>
      </li>
    </ul>
  </section>

</main>
</body>
</html>
```